showcase project portfolio

create power point of project portfolio
from word file and website using similar design template

https://www.brelvon.co.uk/

Target Market(s)

corporte

```html
<!DOCTYPE html>
<html lang="en">
<head>
<meta charset="utf-8">
<title>Brelvon Design Solution – Project Portfolio</title>
<link rel="stylesheet" href="https://fonts.googleapis.com/css2?family=Mulish:wght@300;400;600;700;800&display=swap">
<style>
:root{
  --navy:#1f3b53;
  --navy-deep:#18314a;
  --tan:#c9a183;
  --tan-dark:#a9825f;
  --stage:#dcdadb;
  --white:#ffffff;
  --ink:#2a3f52;
  --photo-a:#b8a497;
  --photo-b:#8f7668;
  --photo-c:#a3a3a6;
  --drawing:#f3f3f1;
}
*{box-sizing:border-box;margin:0;padding:0}
html,body{width:1200px;height:2503px;overflow:hidden;background:var(--stage)}
body{font-family:"Mulish",sans-serif;color:var(--ink)}
.stage{position:absolute;left:0;top:0;width:1235px;height:2576px;transform:scale(.97166);transform-origin:0 0}
.slide{position:absolute;width:556px;height:312px;overflow:hidden;background:var(--white)}
.col-l{left:52px}.col-r{left:627px}
.row-1{top:877px}.row-2{top:1208px}.row-3{top:1539px}.row-4{top:1870px}.row-5{top:2201px}
.hero{left:165px;top:88px;transform:scale(1.625);transform-origin:0 0}

.photo{position:absolute;background:linear-gradient(170deg,var(--photo-c) 0%,var(--photo-a) 35%,var(--photo-b) 70%,var(--photo-c) 100%)}
.photo.green{background:linear-gradient(160deg,#6c7b5a,#8a6c5c 60%,#9b9b9b)}
.photo.brick{background:linear-gradient(175deg,#b48978,#8e5f4d 60%,#a08a80)}
.drawing{position:absolute;background:var(--drawing);border:1px solid #d6d6d2}
.drawing.plan{background:linear-gradient(#f6f2cf,#f1eecd)}

.fade-light{position:absolute;inset:0;background:linear-gradient(90deg,#fff 18%,rgba(255,255,255,.55) 55%,rgba(255,255,255,.15) 100%)}
.fade-dark{position:absolute;inset:0;background:linear-gradient(90deg,var(--navy) 22%,rgba(31,59,83,.6) 60%,rgba(31,59,83,.25) 100%)}

.brand{position:absolute;display:flex;align-items:center;gap:5px;font-weight:800;font-size:15px;letter-spacing:.5px}
.brand .mark{width:9px;height:9px;background:var(--tan)}
.brand.on-light{color:var(--navy)}
.brand.on-dark{color:var(--white)}

.title{position:absolute;left:53px;top:124px;font-weight:800;font-size:30px;line-height:34px}
.subtitle{position:absolute;left:53px;top:199px;font-weight:300;font-size:14px}
.date{position:absolute;left:53px;top:228px;font-size:6px}
.on-light-text{color:var(--navy)}
.on-dark-text{color:var(--white)}

.band{position:absolute;left:0;right:0;bottom:0;height:24px;display:flex;align-items:center;justify-content:center;font-size:5.5px}
.band.gradient{background:linear-gradient(90deg,var(--navy) 0%,#4a5c6b 45%,var(--tan) 100%);color:var(--white)}
.band.plain{background:var(--white);color:var(--ink)}
.band.tan{background:var(--tan);color:var(--ink)}
.title-dark .photo-wrap{position:absolute;left:0;right:0;top:0;bottom:24px}

/* tasks */
.tasks-heading{position:absolute;left:48px;top:39px;font-weight:800;font-size:16px;color:var(--navy);letter-spacing:.5px}
.tasks-rule{position:absolute;left:48px;top:60px;width:50px;height:4px;background:linear-gradient(90deg,var(--tan),#e3d1c3)}
.tasks-band{position:absolute;left:0;top:98px;width:456px;height:150px;background:linear-gradient(90deg,var(--navy) 20%,rgba(120,110,105,.85) 65%,rgba(201,161,131,.9) 100%);display:flex;gap:18px;padding:20px 0 0 48px}
.tasks-band ul{list-style:none;width:170px;color:var(--white);font-size:5.5px;line-height:6.5px}
.tasks-band li{position:relative;margin-bottom:6px;padding-left:12px}
.tasks-band li::before{content:"";position:absolute;left:1px;top:2px;width:2.5px;height:2.5px;border-radius:50%;background:var(--white)}
.corner-copy{position:absolute;right:14px;bottom:18px;font-size:5px;color:var(--white);display:flex;align-items:center;gap:6px}

/* project */
.panel{position:absolute;left:0;top:0;width:217px;height:312px;background:var(--navy)}
.tab{position:absolute;left:0;top:27px;width:230px;height:26px;background:var(--tan);color:var(--white);font-weight:800;font-size:14.5px;letter-spacing:.6px;padding:5px 0 0 28px}
.tab-fold{position:absolute;left:217px;top:53px;width:0;height:0;border-top:10px solid var(--tan-dark);border-right:13px solid transparent}
.info{position:absolute;left:0;width:217px;text-align:center;color:var(--white)}
.info svg{display:block;margin:0 auto 2px}
.info .label{color:var(--tan);font-weight:700;font-size:9.5px;margin-bottom:5px}
.info .text{font-size:6px;line-height:6.6px;padding:0 24px}
.panel .brand{left:16px;bottom:16px;font-size:10px}
.page-copy{position:absolute;right:21px;bottom:15px;font-size:5px;color:var(--ink);display:flex;align-items:center;gap:7px}
.page-num{width:10px;height:10px;background:var(--navy);color:var(--white);font-size:6px;font-weight:700;display:flex;align-items:center;justify-content:center;border-radius:1.5px}

/* contact */
.contact{position:absolute;left:62px;color:var(--white)}
.contact-heading{top:143px;font-weight:800;font-size:9px;letter-spacing:.8px}
.contact-address{top:162px;font-size:6.5px;line-height:7px;width:200px}
.contact-line{display:flex;align-items:center;gap:7px;font-size:6.5px}
.contact-lines{top:192px;display:flex;flex-direction:column;gap:7px}
</style>
</head>
<body>
<svg width="0" height="0" style="position:absolute">
  <defs>
    <symbol id="icon-pin" viewBox="0 0 24 24"><circle cx="12" cy="12" r="11" fill="none" stroke="#fff" stroke-width="1.3"/><path d="M12 5.5a4.3 4.3 0 0 0-4.3 4.3c0 3.2 4.3 8 4.3 8s4.3-4.8 4.3-8A4.3 4.3 0 0 0 12 5.5z" fill="#fff"/><circle cx="12" cy="9.8" r="1.6" fill="#1f3b53"/></symbol>
    <symbol id="icon-bulb" viewBox="0 0 24 24"><circle cx="12" cy="12" r="11" fill="none" stroke="#fff" stroke-width="1.3"/><path d="M12 5.2a4.4 4.4 0 0 0-2.6 8c.5.4.8 1 .8 1.6v.7h3.6v-.7c0-.6.3-1.2.8-1.6a4.4 4.4 0 0 0-2.6-8z" fill="#fff"/><rect x="10.2" y="16.3" width="3.6" height="1.2" fill="#fff"/><rect x="10.8" y="18.1" width="2.4" height="1" fill="#fff"/></symbol>
    <symbol id="icon-phone" viewBox="0 0 24 24"><path d="M6.6 3.5l3 .3 1.3 4-2 1.6a12 12 0 0 0 5.7 5.7l1.6-2 4 1.3.3 3c0 1-1 2-2 2A17.3 17.3 0 0 1 4.6 5.5c0-1 1-2 2-2z" fill="#fff"/></symbol>
    <symbol id="icon-at" viewBox="0 0 24 24"><circle cx="12" cy="12" r="3.6" fill="none" stroke="#fff" stroke-width="2"/><path d="M15.6 12v1.6a2.4 2.4 0 0 0 4.8 0V12a8.4 8.4 0 1 0-3.3 6.7" fill="none" stroke="#fff" stroke-width="2"/></symbol>
    <symbol id="icon-globe" viewBox="0 0 24 24"><g fill="none" stroke="#fff" stroke-width="1.6"><circle cx="12" cy="12" r="9"/><ellipse cx="12" cy="12" rx="4" ry="9"/><path d="M3 12h18M4.5 7.5h15M4.5 16.5h15"/></g></symbol>
  </defs>
</svg>

<main class="stage">

  <!-- Hero title slide -->
  <section class="slide hero">
    <div class="photo" style="inset:0" role="img" aria-label="Street photograph of a brick corner building"></div>
    <div class="fade-light"></div>
    <div class="brand on-light" style="left:53px;top:72px"><span class="mark"></span>Brelvon</div>
    <h1 class="title on-light-text">Brelvon Design<br>Solution</h1>
    <p class="subtitle on-light-text">Project Portfolio</p>
    <p class="date on-light-text">Tuesday, June 4, 2024</p>
    <div class="band gradient">© 2024 Brelvon Design Solution. All rights reserved.</div>
  </section>

  <!-- Title light -->
  <section class="slide col-l row-1">
    <div class="photo" style="inset:0" role="img" aria-label="Street photograph of a brick corner building"></div>
    <div class="fade-light"></div>
    <div class="brand on-light" style="left:53px;top:72px"><span class="mark"></span>Brelvon</div>
    <h2 class="title on-light-text">Brelvon Design<br>Solution</h2>
    <p class="subtitle on-light-text">Project Portfolio</p>
    <p class="date on-light-text">Tuesday, June 4, 2024</p>
    <div class="band gradient">© 2024 Brelvon Design Solution. All rights reserved.</div>
  </section>

  <!-- Title dark -->
  <section class="slide col-r row-1 title-dark">
    <div class="photo-wrap">
      <div class="photo" style="inset:0" role="img" aria-label="Street photograph of a brick corner building"></div>
      <div class="fade-dark"></div>
    </div>
    <div class="brand on-dark" style="left:53px;top:72px"><span class="mark"></span>Brelvon</div>
    <h2 class="title on-dark-text">Brelvon Design<br>Solution</h2>
    <p class="subtitle on-dark-text">Project Portfolio</p>
    <p class="date on-dark-text">Tuesday, June 4, 2024</p>
    <div class="band plain">© 2024 Brelvon Design Solution. All rights reserved.</div>
  </section>

  <!-- Tasks -->
  <section class="slide col-l row-2">
    <div class="photo" style="left:347px;top:0;width:209px;height:312px" role="img" aria-label="Photograph of brick terraced building on a street"></div>
    <h2 class="tasks-heading">TASKS</h2>
    <div class="tasks-rule"></div>
    <div class="tasks-band">
      <ul>
        <li>Creating working drawings</li>
        <li>Price breakdown of total build costs</li>
        <li>Liaising with Norvale Water for water connection, drainage connection</li>
        <li>Liaising with Halwick Gas to get gas supply to site</li>
        <li>Liaising with Corran Power to get electric supply</li>
        <li>Tendering out works to different tradesmen</li>
        <li>Getting material orders</li>
      </ul>
      <ul>
        <li>Arranging structural engineer for the site</li>
        <li>Arranging Building control for the site</li>
        <li>Making sure material is on site on time</li>
        <li>Making sure all tradesman work is up to current British standards</li>
        <li>Daily walk rounds to check work is done according to approved plans</li>
        <li>Placing orders for bathrooms, kitchen, and flooring</li>
        <li>All snag work with main contractor</li>
      </ul>
    </div>
    <div class="brand on-light" style="left:16px;bottom:16px;font-size:11px"><span class="mark"></span>Brelvon</div>
    <div class="corner-copy">© 2024 Brelvon Design Solution. All rights reserved. <span class="page-num" style="background:var(--tan)">2</span></div>
  </section>

  <!-- Project 1 -->
  <section class="slide col-r row-2">
    <div class="panel">
      <div class="info" style="top:68px"><svg width="26" height="26"><use href="#icon-pin"/></svg><p class="label">Location</p><p class="text">Garages at Linden Mews,<br>Linden Street, Derby</p></div>
      <div class="info" style="top:152px"><svg width="26" height="26"><use href="#icon-bulb"/></svg><p class="label">Proposal</p><p class="text">Change of use from garages to two dwelling houses (use class C3) including alterations to the front and side elevations</p></div>
      <div class="brand on-dark"><span class="mark"></span>Brelvon</div>
    </div>
    <div class="tab">PROJECT: 1</div><div class="tab-fold"></div>
    <div class="photo brick" style="left:240px;top:27px;width:180px;height:89px" role="img" aria-label="Photograph of the original garage block"></div>
    <div class="drawing plan" style="left:427px;top:27px;width:103px;height:89px" role="img" aria-label="Floor plan and elevation drawings"></div>
    <div class="photo brick" style="left:240px;top:123px;width:290px;height:150px" role="img" aria-label="Photograph of the completed brick dwellings"></div>
    <div class="page-copy">© 2024 Brelvon Design Solution. All rights reserved. <span class="page-num">4</span></div>
  </section>

  <!-- Project 2 -->
  <section class="slide col-l row-3">
    <div class="panel">
      <div class="info" style="top:68px"><svg width="26" height="26"><use href="#icon-pin"/></svg><p class="label">Location</p><p class="text">48 Fairmead Road, Derby</p></div>
      <div class="info" style="top:152px"><svg width="26" height="26"><use href="#icon-bulb"/></svg><p class="label">Proposal</p><p class="text">Change of use from offices (use class B1) to 12 flats (use class C3)</p></div>
      <div class="brand on-dark"><span class="mark"></span>Brelvon</div>
    </div>
    <div class="tab">PROJECT: 2</div><div class="tab-fold"></div>
    <div class="photo green" style="left:240px;top:27px;width:143px;height:89px" role="img" aria-label="Photograph of the office building behind trees"></div>
    <div class="photo green" style="left:390px;top:27px;width:141px;height:89px" role="img" aria-label="Photograph of the building forecourt"></div>
    <div class="drawing" style="left:240px;top:123px;width:291px;height:149px" role="img" aria-label="Floor plans, sections and schedules for the flats"></div>
    <div class="page-copy">© 2024 Brelvon Design Solution. All rights reserved. <span class="page-num">5</span></div>
  </section>

  <!-- Project 3 -->
  <section class="slide col-r row-3">
    <div class="panel">
      <div class="info" style="top:68px"><svg width="26" height="26"><use href="#icon-pin"/></svg><p class="label">Location</p><p class="text">12-16 Carver Street&nbsp; Derby</p></div>
      <div class="info" style="top:152px"><svg width="26" height="26"><use href="#icon-bulb"/></svg><p class="label">Proposal</p><p class="text">Refurbishment Of Commercial Ground Floor Units Together With Formation Of 6 Residential Units On First And Second Floors. Installation Of Glazing And Repair To External Masonry Including Bricking Up Of Existing Openings</p></div>
      <div class="brand on-dark"><span class="mark"></span>Brelvon</div>
    </div>
    <div class="tab">PROJECT: 3</div><div class="tab-fold"></div>
    <div class="photo" style="left:240px;top:27px;width:141px;height:116px" role="img" aria-label="Photograph of the rendered terrace gable end"></div>
    <div class="photo" style="left:388px;top:27px;width:143px;height:116px" role="img" aria-label="Photograph of the terrace along the street"></div>
    <div class="drawing plan" style="left:240px;top:150px;width:291px;height:122px" role="img" aria-label="Three coloured floor plans with fire routes"></div>
    <div class="page-copy">© 2024 Brelvon Design Solution. All rights reserved. <span class="page-num">6</span></div>
  </section>

  <!-- Project 4 -->
  <section class="slide col-l row-4">
    <div class="panel">
      <div class="info" style="top:68px"><svg width="26" height="26"><use href="#icon-bulb"/></svg><p class="label">Location</p><p class="text">Land At 3 Oakhollow&nbsp; Derby&nbsp; DE24 9RT</p></div>
      <div class="info" style="top:152px"><svg width="26" height="26"><use href="#icon-pin"/></svg><p class="label">Proposal</p><p class="text">Erection of a dwelling house (use class C3)</p></div>
      <div class="brand on-dark"><span class="mark"></span>Brelvon</div>
    </div>
    <div class="tab">PROJECT: 4</div><div class="tab-fold"></div>
    <div class="drawing plan" style="left:240px;top:27px;width:141px;height:243px" role="img" aria-label="Site plan, floor plans and proposed front elevation"></div>
    <div class="photo green" style="left:388px;top:27px;width:143px;height:83px" role="img" aria-label="Photograph of the overgrown plot"></div>
    <div class="photo brick" style="left:388px;top:117px;width:143px;height:153px" role="img" aria-label="Photograph of the completed detached house"></div>
    <div class="page-copy">© 2024 Brelvon Design Solution. All rights reserved. <span class="page-num">7</span></div>
  </section>

  <!-- Project 5 -->
  <section class="slide col-r row-4">
    <div class="panel">
      <div class="info" style="top:68px"><svg width="26" height="26"><use href="#icon-bulb"/></svg><p class="label">Location</p><p class="text">14, Wrenfield Street, Birmingham</p></div>
      <div class="info" style="top:152px"><svg width="26" height="26"><use href="#icon-pin"/></svg><p class="label">Proposal</p><p class="text">Proposal: Warehouse conversion to 4 town houses.</p></div>
      <div class="brand on-dark"><span class="mark"></span>Brelvon</div>
    </div>
    <div class="tab">PROJECT: 5</div><div class="tab-fold"></div>
    <div class="photo brick" style="left:240px;top:27px;width:80px;height:89px" role="img" aria-label="Photograph of the warehouse facade"></div>
    <div class="photo brick" style="left:328px;top:27px;width:78px;height:89px" role="img" aria-label="Photograph of the warehouse courtyard"></div>
    <div class="drawing" style="left:414px;top:27px;width:117px;height:89px" role="img" aria-label="Town house floor plans"></div>
    <div class="photo brick" style="left:240px;top:123px;width:291px;height:149px" role="img" aria-label="Photograph of arched warehouse windows"></div>
    <div class="page-copy">© 2024 Brelvon Design Solution. All rights reserved. <span class="page-num">8</span></div>
  </section>

  <!-- Contact dark -->
  <section class="slide col-l row-5 title-dark">
    <div class="photo-wrap">
      <div class="photo" style="inset:0" role="img" aria-label="Street photograph of a brick corner building"></div>
      <div class="fade-dark"></div>
    </div>
    <div class="brand on-dark" style="left:62px;top:78px"><span class="mark"></span>Brelvon</div>
    <h2 class="contact contact-heading">CONTACT US</h2>
    <p class="contact contact-address">Unit 4 Larkfield Business Park, Ashwell Lane,<br>Derby DE21 7QP</p>
    <div class="contact contact-lines">
      <div class="contact-line"><svg width="9" height="9"><use href="#icon-phone"/></svg>+447700900318</div>
      <div class="contact-line"><svg width="9" height="9"><use href="#icon-at"/></svg>info@brelvon.co.uk</div>
      <div class="contact-line"><svg width="9" height="9"><use href="#icon-globe"/></svg>www.brelvon.co.uk</div>
    </div>
    <div class="band tan">© 2024 Brelvon Design Solution. All rights reserved.</div>
  </section>

  <!-- Contact light band -->
  <section class="slide col-r row-5 title-dark">
    <div class="photo-wrap">
      <div class="photo" style="inset:0" role="img" aria-label="Street photograph of a brick corner building"></div>
      <div class="fade-dark"></div>
    </div>
    <div class="brand on-dark" style="left:62px;top:78px"><span class="mark"></span>Brelvon</div>
    <h2 class="contact contact-heading">CONTACT US</h2>
    <p class="contact contact-address">Unit 4 Larkfield Business Park, Ashwell Lane,<br>Derby DE21 7QP</p>
    <div class="contact contact-lines">
      <div class="contact-line"><svg width="9" height="9"><use href="#icon-phone"/></svg>+447700900318</div>
      <div class="contact-line"><svg width="9" height="9"><use href="#icon-at"/></svg>info@brelvon.co.uk</div>
      <div class="contact-line"><svg width="9" height="9"><use href="#icon-globe"/></svg>www.brelvon.co.uk</div>
    </div>
    <div class="band plain">© 2024 Brelvon Design Solution. All rights reserved.</div>
  </section>

</main>
</body>
</html>
```